Website Landing Page for Medical Recruitment

Looking for a landing page to add to our existing website. The objective of the page is to recruit new clinical staff for various departments within PineHollow Medical Center (non-profit hospital in the Richmond, TX area).

We would like the page to be modern, professional, and non-cluttered. Please include call-to-actions and include a button that will navigate to the page where candidates can submit their applications (this page already exists).

Target Market(s)

25-35-year-olds who live in the Houston and Richmond area with medical experience.

Industry/Entity Type

Medical/Health

Font styles to use
Sans Serif

Colors
0054AA
0677BA
7BADD7
CADEEF
E8F1F8

Requirements
Must have
• A "call to action"; a button that navigates to pinehollowmedcenter.example/careers

```html
<!DOCTYPE html>
<html lang="en">
<head>
<meta charset="utf-8">
<title>Careers – PineHollow Medical Center</title>
<link href="https://fonts.googleapis.com/css2?family=Fira+Sans:wght@600;700&family=Lato:ital,wght@0,400;0,700;1,400&display=swap" rel="stylesheet">
<style>
:root{
  --navy:#0054AA;
  --blue:#0677BA;
  --sky:#7BADD7;
  --mist:#CADEEF;
  --ice:#E8F1F8;
  --cyan:#1ECBE1;
  --indigo:#334C98;
  --ink:#2b2f36;
  --muted:#6b7280;
  --footer:#2B3140;
  --white:#ffffff;
}
*{box-sizing:border-box;margin:0;padding:0}
html,body{width:1200px;height:2991px;overflow:hidden}
body{font-family:"Lato",sans-serif;color:var(--ink);background:#fff;position:relative}
h1,h2,h3,.display{font-family:"Fira Sans",sans-serif;font-weight:700}
a{text-decoration:none;color:inherit}
.abs{position:absolute}

/* top bar */
.topbar{position:absolute;top:0;left:0;width:1200px;height:34px;border-bottom:1px solid #eee;font-size:8.5px;color:#666}
.topbar .items{position:absolute;left:230px;top:12px;display:flex;gap:11px;align-items:center}
.topbar .social{position:absolute;left:889px;top:10px;display:flex;gap:8px}
.topbar .social span{width:11px;height:11px;border-radius:2px;background:#b9bec5;display:block}
.pin{color:var(--sky)}

/* nav */
.nav{position:absolute;top:34px;left:0;width:1200px;height:63px;background:#fff}
.logo{position:absolute;display:flex;align-items:center;gap:6px}
.logo .dot{width:18px;height:18px;border-radius:50%;background:var(--navy)}
.logo .name{font-family:"Lato",sans-serif;font-weight:700;font-size:17px;color:var(--navy)}
.nav .logo{left:228px;top:20px}
.menu{position:absolute;left:420px;top:25px;display:flex;gap:11px;font-size:9px;color:#555;align-items:center}
.menu .alert{color:#e53935}
.menu .active{color:var(--cyan);font-size:10px}
.search{width:9px;height:9px;border:1.5px solid #555;border-radius:50%;margin-left:6px}

/* hero */
.hero{position:absolute;top:97px;left:0;width:1200px;height:535px;background:linear-gradient(100deg,#1e6fc0 0%,#2c86d6 45%,#1b78c8 100%);overflow:hidden}
.hero .photo{position:absolute;left:520px;top:0;width:680px;height:535px;background:linear-gradient(90deg,rgba(30,60,110,0) 0%,#23407a 20%,#2d4f8f 55%,#4aa3e0 78%,#7fc2ea 100%)}
.hero h1{position:absolute;left:225px;top:150px;font-size:44px;line-height:51px;color:#fff}
.btn{display:inline-block;font-family:"Fira Sans",sans-serif;font-weight:600;font-size:12px;border-radius:3px;text-align:center}
.btn-cyan{background:var(--cyan);color:#fff}
.btn-outline{border:2px solid #fff;color:#fff}
.hero .btn{position:absolute;left:225px;top:334px;width:137px;height:41px;line-height:41px}

/* intro */
.intro{position:absolute;top:632px;left:0;width:1200px;height:298px;background:var(--ice)}
.intro h2{position:absolute;left:224px;top:52px;font-size:36px;line-height:46px;color:#2f3337}
.intro .copy{position:absolute;left:581px;top:60px;width:392px;font-size:12.5px;line-height:21px;color:#444}
.intro .copy p+p{margin-top:20px}

/* positions */
.positions{position:absolute;top:930px;left:0;width:1200px;height:775px;background:radial-gradient(circle at 85% 20%,#f1f4f8 0,#fafbfc 40%,#fff 70%)}
.section-title{position:absolute;left:0;width:1200px;text-align:center;font-size:38px;color:#2f3337}
.positions .section-title{top:85px}
.card{position:absolute;border-radius:3px;overflow:hidden;color:#fff}
.card .halo{position:absolute;right:-25px;top:-25px;width:110px;height:110px;border-radius:50%;background:rgba(255,255,255,.08)}
.card .icon{position:absolute;right:20px;top:18px}
.card h3{font-size:20px;line-height:23px}
.card p{font-size:10.5px;line-height:15px;margin-top:8px;opacity:.95}
.card .btn{margin-top:20px;width:86px;height:34px;line-height:30px;font-size:10.5px}
.card .body{position:absolute;left:26px;top:110px;width:200px}
.c1{left:225px;top:177px;width:238px;height:268px;background:var(--blue)}
.c2{left:481px;top:177px;width:238px;height:268px;background:var(--navy)}
.c3{left:737px;top:177px;width:238px;height:268px;background:var(--indigo)}
.c4{left:225px;top:464px;width:494px;height:166px;background:linear-gradient(90deg,#2cc8de,#37cfe3)}
.c4 .photo{position:absolute;left:190px;top:0;width:304px;height:166px;background:linear-gradient(90deg,rgba(255,255,255,0),rgba(120,210,230,.5))}
.c4 .body{left:32px;top:22px}
.c4 .btn{background:var(--navy);border:none;line-height:34px}
.c5{left:737px;top:464px;width:238px;height:166px;background:var(--blue);text-align:center}
.c5 .more{position:absolute;left:0;top:100px;width:238px;font-size:20px}

/* CTA band */
.cta{position:absolute;top:1705px;left:0;width:1200px;height:243px;background:linear-gradient(90deg,#1a6fc0,#1f80cf)}
.cta h2{position:absolute;left:224px;top:47px;font-size:38px;line-height:42px;color:#fff}
.cta .btn{position:absolute;left:224px;top:151px;width:137px;height:41px;line-height:37px}
.cta-photo{position:absolute;left:680px;top:1640px;width:300px;height:308px;border-radius:150px 150px 0 0;background:linear-gradient(180deg,#5a9bd6 0%,#3c86c9 60%,#2a78c2 100%)}

/* testimonials */
.clients .section-title{top:2035px}
.quote{position:absolute;top:2120px;width:359px;height:272px;background:#fff;border:1px solid #e6e9ee;box-shadow:0 4px 14px rgba(0,0,0,.05)}
.quote .marks{position:absolute;right:26px;top:-10px}
.quote .stars{position:absolute;left:35px;top:30px;color:var(--cyan);font-size:15px;letter-spacing:1px}
.quote blockquote{position:absolute;left:35px;top:65px;width:268px;font-style:italic;font-size:15px;line-height:26px;color:#666}
.quote cite{position:absolute;left:35px;top:218px;font-style:normal;font-weight:700;font-size:12.5px;color:#333}
.q1{left:225px}.q2{left:616px}
.arrow{position:absolute;top:2248px}

/* footer */
.footer{position:absolute;top:2582px;left:0;width:1200px;height:409px;background:var(--footer);color:#c7cbd3}
.alert-box{position:absolute;top:2519px;left:141px;width:918px;height:136px;border-radius:14px;background:var(--cyan)}
.alert-box h2{position:absolute;left:84px;top:34px;font-size:40px;color:#fff}
.alert-box .sub{position:absolute;left:84px;top:86px;font-size:12px;color:#fff}
.subscribe{position:absolute;left:446px;top:40px;width:388px;height:54px;background:#fff;border-radius:3px}
.subscribe .ph{position:absolute;left:45px;top:20px;font-size:11px;color:#999}
.subscribe .btn{position:absolute;right:6px;top:6px;width:106px;height:42px;line-height:42px;background:var(--navy);color:#fff;font-size:12px}
.footer .logo{left:225px;top:157px}
.footer .logo .name{color:#fff;font-size:24px}
.footer .logo .dot{background:#fff;width:24px;height:24px}
.about{position:absolute;left:225px;top:215px;width:210px;font-size:10.5px;line-height:16.5px;color:#9aa0ab}
.fcol{position:absolute;top:136px}
.fcol h4{font-family:"Fira Sans",sans-serif;font-weight:600;font-size:11px;letter-spacing:.5px;color:#9aa0ab;margin-bottom:18px}
.fcol li{list-style:none;font-size:10.5px;color:#fff;margin-bottom:12px}
.jobs{left:560px}
.contact{left:817px}
.contact .row{display:flex;gap:8px;font-size:9.5px;line-height:14px;color:#fff;margin-bottom:10px;align-items:flex-start}
.contact .phone{font-family:"Fira Sans",sans-serif;font-weight:600;font-size:14px}
.contact .mail{color:var(--cyan);font-size:10.5px}
.copyright{position:absolute;left:225px;top:356px;width:750px;border-top:1px solid #3b4252;padding-top:15px;text-align:center;font-size:10px;color:#9aa0ab}
</style>
</head>
<body>

<header class="topbar">
  <div class="items">
    <span><span class="pin">●</span> 2410 Cedar Lane, Alder Springs, Colorado</span>
    <span>Call: 555-014-2300</span>
    <span>Careers</span>
    <span>Physician/Staff Login</span>
    <span>Patient Portal</span>
    <span>Pay My Bill</span>
    <span>Contact Us ▾</span>
    <span>PineHollow Medical Group ▾</span>
  </div>
  <div class="social"><span></span><span></span><span></span><span></span></div>
</header>

<nav class="nav">
  <a class="logo" href="#"><span class="dot"></span><span class="name">PineHollow</span></a>
  <div class="menu">
    <span>Home</span><span>Find A Doctor</span><span class="alert">COVID-19</span><span>About Us</span><span>Services</span><span>Locations</span><span>Patients/Visitors</span><span>Ways To Give</span><span>Health Library</span><span class="active">Career</span><span class="search"></span>
  </div>
</nav>

<section class="hero">
  <div class="photo" role="img" aria-label="Photo of a line of clinical staff in scrubs with stethoscopes"></div>
  <h1>We are<br>Looking to Hire<br>Clinical Staff</h1>
  <a class="btn btn-cyan" href="https://pinehollowmedcenter.example/careers">Become a Member</a>
</section>

<section class="intro">
  <h2>Find Healthcare<br>Job Remotely</h2>
  <div class="copy">
    <p>Lorem ipsum dolor sit amet, consectetur adipiscing elit, sed do eiusmod tempor incididunt ut labore et dolore magna aliqua. Ut enim ad minim veniam, quis nostrud exercitation ullamco laboris nisi ut aliquip ex ea commodo consequat.</p>
    <p>Duis aute irure dolor in reprehenderit in voluptate velit esse cillum dolore eu fugiat nulla pariatur. Excepteur sint occaecat cupidatat non proident sunt in culpa qui officia deserunt.</p>
  </div>
</section>

<section class="positions">
  <h2 class="section-title">Positions We Have Available</h2>

  <article class="card c1">
    <span class="halo"></span>
    <svg class="icon" width="44" height="44" viewBox="0 0 44 44" fill="none" stroke="#fff" stroke-width="2"><circle cx="22" cy="15" r="8"/><path d="M8 40c0-8 6-13 14-13s14 5 14 13z"/><path d="M19 33h6M22 30v6"/></svg>
    <div class="body"><h3>Certified Nurses Assistants</h3><p>Consectetur adipisicing elit, sed do eiu smod tempor incididunt.</p><a class="btn btn-outline" href="https://pinehollowmedcenter.example/careers">Apply Now</a></div>
  </article>

  <article class="card c2">
    <span class="halo"></span>
    <svg class="icon" width="44" height="44" viewBox="0 0 44 44" fill="none" stroke="#fff" stroke-width="2"><path d="M12 36V24a10 10 0 0 1 20 0v12"/><path d="M8 36h28v4H8z"/><path d="M22 4v5M8 10l3 3M36 10l-3 3M4 22h4M36 22h4"/></svg>
    <div class="body"><h3>Emergency Room Techs</h3><p>Consectetur adipisicing elit, sed do eiu smod tempor incididunt.</p><a class="btn btn-outline" href="https://pinehollowmedcenter.example/careers">Apply Now</a></div>
  </article>

  <article class="card c3">
    <span class="halo"></span>
    <svg class="icon" width="44" height="44" viewBox="0 0 44 44" fill="none" stroke="#fff" stroke-width="2"><path d="M10 6h24v10H10z"/><path d="M22 8v6M19 11h6"/><path d="M12 16v10a10 10 0 0 0 20 0V16"/><path d="M6 42c0-7 7-10 16-10s16 3 16 10z"/></svg>
    <div class="body"><h3>Licensed Vocational Nurses</h3><p>Consectetur adipisicing elit, sed do eiu smod tempor incididunt.</p><a class="btn btn-outline" href="https://pinehollowmedcenter.example/careers">Apply Now</a></div>
  </article>

  <article class="card c4">
    <div class="photo" role="img" aria-label="Faint photo of smiling nurses"></div>
    <span class="halo"></span>
    <svg class="icon" width="44" height="44" viewBox="0 0 44 44" fill="none" stroke="#fff" stroke-width="2"><path d="M10 6h24v10H10z"/><path d="M22 8v6M19 11h6"/><path d="M12 16v10a10 10 0 0 0 20 0V16"/><path d="M6 42c0-7 7-10 16-10s16 3 16 10z"/></svg>
    <div class="body"><h3>Registered Nurses</h3><p>Consectetur adipisicing elit, sed do eiu smod tempor incididunt.</p><a class="btn" href="https://pinehollowmedcenter.example/careers">Apply Now</a></div>
  </article>

  <a class="card c5" href="https://pinehollowmedcenter.example/careers">
    <svg class="abs" style="left:105px;top:53px" width="28" height="28" viewBox="0 0 28 28" fill="none" stroke="#fff" stroke-width="2"><rect x="2" y="2" width="10" height="10" rx="2"/><rect x="16" y="2" width="10" height="10" rx="2"/><rect x="2" y="16" width="10" height="10" rx="2"/><circle cx="21" cy="21" r="5"/></svg>
    <span class="more display">MORE</span>
  </a>
</section>

<section class="cta">
  <h2>Get the Clinical Job<br>You Want</h2>
  <a class="btn btn-outline" href="https://pinehollowmedcenter.example/careers">Become a Member</a>
</section>
<div class="cta-photo" role="img" aria-label="Photo of a smiling doctor in a white coat with arms crossed"></div>

<section class="clients">
  <h2 class="section-title">What Our Clients Say</h2>
  <svg class="arrow" style="left:142px" width="22" height="16" viewBox="0 0 22 16" fill="none" stroke="#333" stroke-width="2"><path d="M21 8H2M8 2L2 8l6 6"/></svg>
  <article class="quote q1">
    <svg class="marks" width="30" height="20" viewBox="0 0 30 20" fill="#0054AA"><circle cx="7" cy="7" r="6.5"/><path d="M13 7c0 7-5 12-11 13 4-3 6-6 6-10z"/><circle cx="22" cy="7" r="6.5"/><path d="M28 7c0 7-5 12-11 13 4-3 6-6 6-10z"/></svg>
    <div class="stars">★★★★★</div>
    <blockquote>“Glad to have had the convenience of care and not have to travel out of town. The entire staff on duty that day was so accommodating and pleasant!”</blockquote>
    <cite>- Lakeside Emergency Room Patient</cite>
  </article>
  <article class="quote q2">
    <svg class="marks" width="30" height="20" viewBox="0 0 30 20" fill="#0054AA"><circle cx="7" cy="7" r="6.5"/><path d="M13 7c0 7-5 12-11 13 4-3 6-6 6-10z"/><circle cx="22" cy="7" r="6.5"/><path d="M28 7c0 7-5 12-11 13 4-3 6-6 6-10z"/></svg>
    <div class="stars">★★★★★</div>
    <blockquote>“Everyone from the moment we checked in, until I was discharged, was extremely professional and helpful. Thank you for taking great care of me and easing my worried husband’s mind!”</blockquote>
    <cite>- Emergency Room Patient</cite>
  </article>
  <svg class="arrow" style="left:1036px" width="22" height="16" viewBox="0 0 22 16" fill="none" stroke="#333" stroke-width="2"><path d="M1 8h19M14 2l6 6-6 6"/></svg>
</section>

<footer class="footer">
  <a class="logo" href="#"><span class="dot"></span><span class="name">PineHollow</span></a>
  <p class="about">On March 14, 1952, at the invitation of Mr. and Mrs. H.L. Morrow, the following people met at the H.L. Morrow farm for the purpose of organizing and establishing a hospital in Cedar Valley County.</p>
  <div class="fcol jobs">
    <h4>AVAILABLE JOBS</h4>
    <ul><li>Certified Nurses Assistants</li><li>Emergency Room Techs</li><li>Licensed Vocational Nurses</li><li>Registered Nurses</li><li>Unit Secretaries</li><li>More!</li></ul>
  </div>
  <div class="fcol contact">
    <h4>CONTACT US</h4>
    <div class="row"><svg width="12" height="14" viewBox="0 0 12 14" fill="none" stroke="#fff" stroke-width="1.3"><path d="M6 13S1 8 1 5a5 5 0 0 1 10 0c0 3-5 8-5 8z"/><circle cx="6" cy="5" r="1.8"/></svg><span>PineHollow Medical Center<br>Cedar Lane Hospital Campus<br>2410 Cedar Lane, Alder Springs<br>Colorado 80910</span></div>
    <div class="row"><svg width="13" height="13" viewBox="0 0 13 13" fill="none" stroke="#fff" stroke-width="1.3"><path d="M3 1l2 3-1.5 1.5a7 7 0 0 0 4 4L9 8l3 2-1 2C6 12 1 7 1 2z"/></svg><span class="phone">555-014-2300</span></div>
    <div class="row"><svg width="13" height="10" viewBox="0 0 13 10" fill="none" stroke="#1ECBE1" stroke-width="1.2"><rect x=".6" y=".6" width="11.8" height="8.8"/><path d="M1 1l5.5 4.5L12 1"/></svg><span class="mail">info@phmc.example</span></div>
    <div class="row"><svg width="13" height="10" viewBox="0 0 13 10" fill="none" stroke="#1ECBE1" stroke-width="1.2"><rect x=".6" y=".6" width="11.8" height="8.8"/><path d="M1 1l5.5 4.5L12 1"/></svg><span class="mail">jobs@phmc.example</span></div>
  </div>
  <p class="copyright">Copyright PineHollow 2022-23 | Proudly Powered By Northfield Web Services LLC | Privacy Policy | Refund Policy | Public Information Request</p>
</footer>

<section class="alert-box">
  <h2>Job Alert</h2>
  <p class="sub">Get latest Job Alerts directly to your inbox</p>
  <form class="subscribe">
    <svg class="abs" style="left:20px;top:22px" width="15" height="11" viewBox="0 0 15 11" fill="none" stroke="#999" stroke-width="1.2"><rect x=".6" y=".6" width="13.8" height="9.8"/><path d="M1 1l6.5 5L14 1"/></svg>
    <span class="ph">Enter Your Email Address</span>
    <span class="btn">Subscribe</span>
  </form>
</section>

</body>
</html>
```